the look of import selling star-up company

I have attached rhino logo that i like (can be edit) and i wanna turn that in to luxury look. Example like black base and gold logo +luxury looking font.

Company name: Aurelo trading Oy
Slogan: Ordinary is not an option.
CEO Juho Kettumaa
Starting to import ceramic nano coatings to cars, in home use and industrial purposes.

Target Market(s)

30-60 year old men and women ho have big money and know what car they drive

Industry/Entity Type

It Company

```html
<!DOCTYPE html>
<html lang="en">
<head>
<meta charset="utf-8">
<title>Aurelo trading Oy – Business Card</title>
<link href="https://fonts.googleapis.com/css2?family=Roboto:wght@400;500;700&display=swap" rel="stylesheet">
<style>
  :root {
    --bg: #3a322e;
    --ink: #1d2126;
    --card-black: #1f2328;
    --gold-light: #f3d64a;
    --gold: #d9aa1c;
    --gold-deep: #b0820e;
    --gold-text: #d4a520;
  }
  * { box-sizing: border-box; margin: 0; padding: 0; }
  html, body {
    width: 1200px; height: 769px; overflow: hidden;
    background: var(--bg);
    font-family: "Roboto", Arial, sans-serif;
  }
  .canvas {
    position: relative; width: 1200px; height: 769px;
    display: flex; align-items: center; justify-content: center; gap: 60px;
  }
  .card {
    position: relative; width: 520px; height: 297px; overflow: hidden;
    box-shadow: 0 14px 30px rgba(0,0,0,.45);
  }
  .card--front {
    background: linear-gradient(115deg, var(--gold-deep) 0%, var(--gold) 30%, var(--gold-light) 55%, var(--gold) 80%, var(--gold-deep) 100%);
  }
  .card--back { background: var(--card-black); }

  .front__seal {
    position: absolute; right: -110px; top: -62px;
    width: 420px; height: 420px; border-radius: 50%;
    border: 8px solid var(--ink);
    display: flex; align-items: center; justify-content: center;
  }
  .front__seal-disc {
    width: 364px; height: 364px; border-radius: 50%;
    background: var(--ink);
    display: flex; align-items: center; justify-content: center;
    padding-right: 96px;
  }
  .brand-name {
    font-weight: 700; font-size: 21px; color: var(--gold-text);
    letter-spacing: .5px; text-align: center; line-height: 1.2;
    white-space: nowrap;
  }

  .front__details {
    position: absolute; left: 30px; top: 38px; color: var(--ink);
  }
  .person__name { font-weight: 700; font-size: 19px; letter-spacing: .4px; text-transform: uppercase; }
  .person__role { font-size: 13px; margin-top: 2px; }
  .address { font-size: 12.5px; line-height: 1.3; margin-top: 22px; }
  .contacts { list-style: none; margin-top: 12px; font-size: 12.5px; }
  .contacts li { display: flex; align-items: center; gap: 8px; height: 18px; }
  .contacts svg { width: 13px; height: 13px; flex: none; }
  .slogan { font-weight: 700; font-size: 13.5px; margin-top: 14px; }

  .back__mark {
    position: absolute; inset: 0;
    display: flex; flex-direction: column; align-items: center; justify-content: center; gap: 14px;
  }
  .back__ring {
    width: 70px; height: 70px; border-radius: 50%;
    border: 8px solid var(--gold);
  }
  .card--back .brand-name { color: var(--gold); font-size: 20px; }
</style>
</head>
<body>
<main class="canvas">
  <section class="card card--front" aria-label="Card front">
    <div class="front__seal">
      <div class="front__seal-disc">
        <span class="brand-name">Aurelo trading Oy</span>
      </div>
    </div>
    <div class="front__details">
      <h1 class="person__name">Juho Kettumaa</h1>
      <p class="person__role">CEO</p>
      <p class="address">2140 Harbor Street<br>Juneau, Alaska 99801</p>
      <ul class="contacts">
        <li><svg viewBox="0 0 14 14"><circle cx="7" cy="7" r="7" fill="#1d2126"/><path d="M4.5 3.8l1.3-.3.8 1.8-.8.6a5 5 0 0 0 2.3 2.3l.6-.8 1.8.8-.3 1.3C7 9.8 4 7 4.5 3.8z" fill="#e6bd2c"/></svg>555 210 4417</li>
        <li><svg viewBox="0 0 14 14"><circle cx="7" cy="7" r="7" fill="#1d2126"/><rect x="5" y="3.3" width="4" height="7.4" rx=".7" fill="#e6bd2c"/></svg>555 382 9071</li>
        <li><svg viewBox="0 0 14 14"><circle cx="7" cy="7" r="7" fill="#1d2126"/><rect x="3.8" y="5.5" width="6.4" height="4.2" fill="#e6bd2c"/><rect x="5" y="3.5" width="4" height="2" fill="#e6bd2c"/></svg>555 764 2285</li>
        <li><svg viewBox="0 0 14 14"><circle cx="7" cy="7" r="7" fill="#1d2126"/><rect x="3.5" y="4.5" width="7" height="5" fill="#e6bd2c"/><path d="M3.5 4.5L7 7.4l3.5-2.9" stroke="#1d2126" stroke-width=".8" fill="none"/></svg>juho@aurelotrading.com</li>
        <li><svg viewBox="0 0 14 14"><circle cx="7" cy="7" r="7" fill="#1d2126"/><circle cx="7" cy="7" r="3.5" fill="none" stroke="#e6bd2c" stroke-width="1"/><path d="M3.5 7h7M7 3.5v7" stroke="#e6bd2c" stroke-width=".8"/></svg>www.aurelotrading.com</li>
      </ul>
      <p class="slogan">Ordinary is not an option.</p>
    </div>
  </section>

  <section class="card card--back" aria-label="Card back">
    <div class="back__mark">
      <div class="back__ring"></div>
      <span class="brand-name">Aurelo trading Oy</span>
    </div>
  </section>
</main>
</body>
</html>
```